Presentation card Venture KELO - Tech Incubator from Perú

We need a Design to promote the incubator of technology Startups.
We are in Perú, we work with a string tech filter and develop enterprenurship competencies in the Startup team.
The card is to facilitators and staff memebers of VentureKELO.
We want a clear, modern, tech and agile Design.

We work to help New enterprises of technology here in Perú, we expect the candidates have a big competencies to Research and develop technological products.

We work using methodologies from QRB, Folmestry, Brakewell and Harrowgate univeesities. Our book base is the disciplina of enterpreneur.

We work events all year using diferent formats: Brightforge, Vorne price, OPRA Model Competition you can use these logros in your Design.

Set the name, role, email, cell phone number, address.

Example:
// Contact info section
Tobías Quiroveda
Swift Modeling Hub Manager
tobias.quiroveda@kelo-example.pe
(511) 999 000 417

// Address info section
VentureKELO
Technology-based business incubator
Av. Los Cedrales 884, Valdora
Lima - Perú
web: venture-kelo-example.org.pe
email: venture@kelo-example.pe
phone number: (511) 3926508 ext. 4418

// (optional)Lema section
Making happy using technology

// Social network section
facebook: venturekelooficial

Target Market(s)

Enterprenurship, CTO, Investors, Companies interested on open innovation services

Industry/Entity Type

Information Technology

Contact Information for Business Card

Name, Role, Email, Cell phone number

Colors

Designer to choose colors to be used in the design.

Requirements
Must have
• Logo forms and colors
Nice to have
• I add pictures of the leaders of incubator
Should not have
• No vertical designs

```html
<!DOCTYPE html>
<html lang="es">
<head>
<meta charset="utf-8">
<title>Venture KELO – Business Card</title>
<link rel="stylesheet" href="https://fonts.googleapis.com/css2?family=Josefin+Sans:wght@300;400;600;700&display=swap">
<style>
  :root {
    --crimson: #b83356;
    --paper: #ffffff;
    --ink: #2b2b2b;
    --on-crimson: #ffffff;
    --on-crimson-soft: rgba(255, 255, 255, 0.88);
    --page: #e9e9e9;
  }
  * { box-sizing: border-box; margin: 0; padding: 0; }
  html, body {
    width: 1200px;
    height: 686px;
    overflow: hidden;
    background: var(--page);
  }
  .card {
    position: relative;
    width: 1200px;
    height: 686px;
    background: var(--paper);
    overflow: hidden;
    font-family: "Josefin Sans", sans-serif;
  }
  .brand {
    position: absolute;
    left: 120px;
    top: 262px;
    display: flex;
    align-items: center;
    gap: 20px;
  }
  .brand-mark {
    width: 22px;
    height: 22px;
    background: var(--crimson);
    flex: none;
  }
  .brand-name {
    color: var(--ink);
    font-weight: 700;
    font-size: 60px;
    line-height: 1.02;
    letter-spacing: 0.5px;
  }
  .panel-shadow {
    position: absolute;
    inset: 0;
    filter: drop-shadow(-10px 0 16px rgba(0, 0, 0, 0.38));
  }
  .panel {
    position: absolute;
    inset: 0;
    background: var(--crimson);
    clip-path: polygon(666px 0, 1200px 0, 1200px 686px, 423px 686px);
  }
  .contact {
    position: absolute;
    left: 640px;
    top: 310px;
    width: 515px;
    color: var(--on-crimson);
  }
  .contact-name {
    text-align: center;
    font-weight: 600;
    font-size: 34px;
    letter-spacing: 1px;
  }
  .name-rule {
    height: 16px;
    margin: 8px auto 0;
    width: 470px;
    background: radial-gradient(ellipse at center top, rgba(0, 0, 0, 0.28) 0%, rgba(0, 0, 0, 0) 70%);
  }
  .contact-role {
    margin-top: 22px;
    text-align: center;
    font-weight: 300;
    font-size: 20px;
    letter-spacing: 0.6px;
    color: var(--on-crimson-soft);
  }
  .contact-lines {
    position: absolute;
    left: 724px;
    top: 500px;
    list-style: none;
    color: var(--on-crimson);
  }
  .contact-line {
    display: flex;
    align-items: center;
    height: 40px;
    margin-bottom: 23px;
    font-weight: 300;
    font-size: 21px;
    letter-spacing: 0.3px;
  }
  .contact-icon {
    width: 30px;
    height: 30px;
    margin-right: 40px;
    flex: none;
  }
</style>
</head>
<body>
  <main class="card">
    <div class="brand">
      <span class="brand-mark"></span>
      <div class="brand-name">Venture<br>KELO</div>
    </div>

    <div class="panel-shadow"><div class="panel"></div></div>

    <section class="contact">
      <h1 class="contact-name">Tobías Quiroveda</h1>
      <div class="name-rule"></div>
      <p class="contact-role">Swift Modeling Hub Manager</p>
    </section>

    <ul class="contact-lines">
      <li class="contact-line">
        <svg class="contact-icon" viewBox="0 0 24 24" aria-hidden="true">
          <path fill="#fff" d="M9 2.5c.8-.4 1.6 0 1.9.7l1.2 3.3c.3.7 0 1.5-.6 1.9l-1.3.8c-.3.2-.4.6-.3.9.5 1.9 1.3 3.6 2.5 5.1.2.3.6.4.9.2l1.4-.6c.7-.3 1.5-.1 1.9.5l1.9 2.9c.4.7.2 1.5-.4 1.9l-1.6 1.1c-1 .7-2.4.8-3.5.1C8.6 18.4 5.8 13.7 5.6 8c0-1.3.7-2.5 1.8-3.1z"/>
        </svg>
        <span>(511) 999 000 417</span>
      </li>
      <li class="contact-line">
        <svg class="contact-icon" viewBox="0 0 30 22" aria-hidden="true">
          <rect x="1" y="2" width="28" height="18" fill="#fff"/>
          <path d="M1 2l14 11L29 2M1 20l10-9M29 20l-10-9" fill="none" stroke="#b83356" stroke-width="1.6"/>
        </svg>
        <span>tobias.quiroveda@kelo-example.pe</span>
      </li>
    </ul>
  </main>
</body>
</html>
```